Brizzles - Inspiring Biscuits - Food for thought!

We have a current website but have had a complete redesign of our logo and look. We need to bring the site up to scratch with this new look and feel.
Brizzle Brief
I have attached the concept document.
• Brizzles – Inspiring Biscuits are the reinvented fortune cookie. Individually wrapped cookies with a motivational message stuck on the outside. They are fun, often cheeky, thought provoking and yum.
• Initially we want to focus on just the adult quote range but will over time add the Brizzle kids range. Where we are at at the moment is we have the concept for the Brizzle kids but are lining up a graphic artist to design individual pictures for the kids range. We do not own the ones for the kids pics at the moment so are unable to use those specific ones.
• If however you are able to source almost identical ones that we can use for the website without any licensing issues then please feel free to talk to me about this and send some examples.
• We are only at this stage selling in bulk boxes of 60 Brizzles so want a simple shopping cart where we can add to over time. The long term goal is retail.
• I post a quote daily on facebook and have a long winded manual process where I then upload on to linkedin, pinterest, and twitter. I would like to be able to load a quote of the day on to our website and it updates all the rest for me. On FB, plain circle and plain circle we are Brizzlebiscuits.
• I would also like to be able to use this as a blog – assume it’s the same thing if I am uploading a picture.
• I would like something clean and funky and something we can build on especially when we start going down the path of the kids brizzles as I would in the long term like to get an interactive site for kids to play on and we have all the characters on our Brizzles for the kids to play with.
Based on how we go we may look to crowdfund, so think about this possibility as we will want the website to link in to that if need be.
I am not a control freak and love people whose imagination runs wild. The only restraints I have are the colours that are in the uploaded PDF, the logos used and fonts the designers have selected. The main one used on the quote labels is Avian Bold.
Fonts are :-
apple braille outline 6 dot
avianbol
avianreg
kidsscript - bold
lubalgraboo
lubalingraph - book
I have uploaded what I think you might need to get started, however please feel free to send as many questions you can think of.
Cheers
Fiona
Updates
i have uploaded a load more info and files for the site brief.
Reason: I have had quite a few acceptance and as I am new to this site don't want to upset anyone who has accepted but run out of time.
Thanks to those who have submitted so far we are looking at all of them next week, no one is ruled out at this point. Have to say there are some very talented people out there.
We really appreciate the response and imaginations. Keep you posted
Fiona
Target Market(s)
Anyone that likes motivation. While brizzles are motivational cookies, we are actually in the motivation business not the cookie business.
Industry/Entity Type
Shopping
Requirements
Must have
- Ecommerce - shopping cart
Links to social media twitter, facebook, plain circle, linkedin the more the merrier.

```html
<!DOCTYPE html>
<html lang="en">
<head>
<meta charset="utf-8">
<title>Brizzles - Inspiring Biscuits</title>
<link href="https://fonts.googleapis.com/css2?family=Cabin:wght@400;500;600;700&display=swap" rel="stylesheet">
<style>
:root{
  --page:#b5ca84;
  --nav:#65832a;
  --nav-active:#55731f;
  --band:#849f46;
  --footer:#6d8a33;
  --bar:#85a04b;
  --ink:#1c1c1c;
  --white:#ffffff;
  --cream:#f4eedc;
  --frame:#c3161c;
  --frame-dark:#8c0d12;
  --green:#9cc27a;
  --orange:#e9a14a;
  --red:#ee6a55;
  --blue:#7eadd6;
  --gold:#f7b500;
  --gold-light:#ffd640;
}
*{margin:0;padding:0;box-sizing:border-box}
html,body{width:1012px;height:1200px;overflow:hidden}
body{background:var(--page);font-family:'Cabin',sans-serif;color:var(--ink);position:relative}
.abs{position:absolute}

.site-nav{position:absolute;left:0;top:0;width:1012px;height:38px;background:var(--nav)}
.site-nav a{position:absolute;top:0;line-height:38px;color:var(--white);text-decoration:none;font-size:10px;font-weight:500;letter-spacing:.2px}
.site-nav .active{left:153px;width:85px;background:var(--nav-active);text-align:center}
.site-nav .small{font-size:8px}
.site-nav .sep{position:absolute;top:15px;width:1px;height:8px;background:var(--white)}

.brand{position:absolute;left:0;width:1012px;text-align:center}
.brand-name{top:52px;font-size:72px;font-weight:700;letter-spacing:-2px;line-height:80px}
.brand-tag{top:142px;font-size:18px;font-weight:600;letter-spacing:1px}

.hero{position:absolute;left:154px;top:186px;width:704px;height:302px;border-radius:14px;background:linear-gradient(#d8242a,var(--frame) 60%,var(--frame-dark));box-shadow:0 5px 6px rgba(0,0,0,.35)}
.hero-photo{position:absolute;left:13px;top:14px;width:679px;height:276px;border-radius:10px;background:radial-gradient(ellipse at 50% 40%,#8a5a48,#6b3f30 60%,#4f2c22)}
.sticker{position:absolute;top:56px;width:130px;height:130px;border-radius:50%;background:var(--cream);box-shadow:0 2px 4px rgba(0,0,0,.4)}
.sticker-face{position:absolute;left:9px;top:9px;width:112px;height:112px;border-radius:50%;text-align:center;color:var(--ink)}
.sticker-url{position:absolute;left:0;top:1px;width:130px;text-align:center;font-size:5px}
.sticker-quote{position:absolute;left:14px;top:24px;width:84px;font-size:7px;line-height:10px;text-transform:uppercase}
.sticker-name{position:absolute;left:0;top:72px;width:112px;font-size:14px;font-weight:700;letter-spacing:-.5px}
.hero-title{position:absolute;left:0;top:386px;width:1012px;text-align:center;font-size:46px;font-weight:700;letter-spacing:-2px;color:var(--white)}

.dots{position:absolute;left:493px;top:506px}
.dots span{display:inline-block;width:8px;height:8px;border-radius:50%;background:#8a8f86;margin-right:3.6px}
.dots .on{background:#5b8d1a}

.welcome{position:absolute;left:0;top:530px;width:1012px;text-align:center}
.welcome .lead{font-size:19px;font-weight:500}
.welcome .name{font-size:34px;font-weight:700;letter-spacing:-1px}
.intro{position:absolute;left:163px;width:686px;text-align:center;font-size:8.6px;line-height:13px}

.accordion{position:absolute;left:153px;top:678px;width:707px;height:40px;border-radius:10px;background:var(--bar);border:1px solid #6f8c35}
.accordion-title{position:absolute;left:26px;top:10px;font-size:14px;font-weight:500;color:var(--white)}
.accordion-toggle{position:absolute;right:6px;top:5px;width:37px;height:28px;border-radius:14px;background:#6e8a35}

.section-title{position:absolute;left:0;top:736px;width:1012px;text-align:center;font-size:20px;font-weight:500;color:var(--white)}

.band{position:absolute;left:0;top:782px;width:1012px;height:352px;background:var(--band)}
.product{position:absolute;top:822px;width:162px}
.product-name{width:162px;text-align:center;font-size:22px;font-weight:700;color:var(--white);letter-spacing:-1px;line-height:26px}
.product-card{position:absolute;top:24px;left:0;width:162px;height:156px;border-radius:10px;background:var(--white)}
.product-photo{position:absolute;left:16px;top:34px;width:130px;height:92px;border-radius:4px;background:linear-gradient(#f2f2f2,#dcdcdc)}
.product-photo i{position:absolute;left:38px;top:19px;width:54px;height:54px;border-radius:50%;border:4px solid #6a3c2c}
.product-caption{position:absolute;top:197px;width:162px;text-align:center;font-size:10px;line-height:15px;font-weight:500;color:var(--cream)}
.add-to-cart{position:absolute;top:248px;left:21px;width:120px;height:28px;border-radius:7px;background:linear-gradient(var(--gold-light),var(--gold));box-shadow:0 2px 2px rgba(0,0,0,.25);text-align:center;line-height:28px;font-size:11px;font-weight:600;color:var(--white)}

.site-footer{position:absolute;left:0;top:1134px;width:1012px;height:66px;background:var(--footer);color:var(--white)}
.footer-links{position:absolute;left:153px;top:21px;font-size:7px}
.footer-links span{margin-right:13px}
.copyright{position:absolute;left:153px;top:39px;font-size:6.5px}
.follow{position:absolute;left:681px;top:30px;font-size:7px}
.social{position:absolute;top:21px;width:28px;height:28px;border-radius:50%}
</style>
</head>
<body>

<nav class="site-nav">
  <a class="active">HOME</a>
  <a style="left:265px">ABOUT US</a>
  <a style="left:365px">PRODUCTS</a>
  <a style="left:468px">SEND US A SIGN</a>
  <a class="small" style="left:674px">MY ACCOUNT</a>
  <span class="sep" style="left:744px"></span>
  <a class="small" style="left:766px">LOGIN</a>
  <span class="sep" style="left:812px"></span>
  <a class="small" style="left:833px">SIGN UP</a>
</nav>

<div class="brand brand-name">brizzles</div>
<div class="brand brand-tag">INSPIRING BISCUITS</div>

<section class="hero">
  <div class="hero-photo" role="img" aria-label="Close-up photo of a chocolate biscuit"></div>
  <div class="sticker" style="left:54px"><div class="sticker-face" style="background:var(--green)"><div class="sticker-quote">Success is often achieved by those who don't know that failure is inevitable.</div><div class="sticker-name">brizzles</div></div><div class="sticker-url">www.brizzlebiscuits.com</div></div>
  <div class="sticker" style="left:214px"><div class="sticker-face" style="background:var(--orange)"><div class="sticker-quote" style="top:28px">Learn the rules of the game - then play better than anyone else.</div><div class="sticker-name">brizzles</div></div><div class="sticker-url">www.brizzlebiscuits.com</div></div>
  <div class="sticker" style="left:373px"><div class="sticker-face" style="background:var(--red)"><div class="sticker-quote" style="top:28px">Dreams come true if you can survive the hard times.</div><div class="sticker-name">brizzles</div></div><div class="sticker-url">www.brizzlebiscuits.com</div></div>
  <div class="sticker" style="left:532px"><div class="sticker-face" style="background:var(--blue)"><div class="sticker-quote" style="top:28px">If you're far from the enemy, make him believe you are near.</div><div class="sticker-name">brizzles</div></div><div class="sticker-url">www.brizzlebiscuits.com</div></div>
</section>
<div class="hero-title">Inspiring Biscuits</div>

<div class="dots"><span class="on"></span><span></span><span></span><span></span><span></span></div>

<div class="welcome"><span class="lead">Welcome to </span><span class="name">brizzles</span></div>
<p class="intro" style="top:582px">A long time ago in a country far far away a very clever person invented the fortune cookie. Many many years later a couple of wise but demotivated women in New Zealand were munching some plain old cookies &amp; reading motivational quotes for fun.</p>
<p class="intro" style="top:621px">The day progressed &amp; the quotes became more inspiring. They started playing with the words biscuits &amp; inspiring. Then came this quote "Everything has been thought of before. The difficulty is to think of it again" They stopped munching looked at each other &amp; laughed out loud, for the love of chocolate!</p>

<div class="accordion">
  <div class="accordion-title">BRIZZLES: Adults biscuit sticker concepts</div>
  <div class="accordion-toggle"><svg width="37" height="28" viewBox="0 0 37 28"><path d="M12 11h13l-6.5 8z" fill="#b5ca84"/></svg></div>
</div>

<div class="section-title">BRIZZLES: Adults biscuit sticker concepts</div>

<div class="band"></div>
<svg class="abs" style="left:460px;top:781px" width="100" height="24" viewBox="0 0 100 24"><path d="M0 1C25 1 35 22 50 22S75 1 100 1V0H0z" fill="var(--page)"/></svg>

<div class="product" style="left:153px"><div class="product-name">brizzles</div><div class="product-card"><div class="product-photo" role="img" aria-label="Wrapped biscuit with a green quote sticker"><i style="background:var(--green)"></i></div></div><div class="product-caption">SUCCESS IS OFTEN ACHIEVED BY THOSE WHO DON'T KNOW THAT FAILURE IS INEVITABLE.</div><div class="add-to-cart">ADD TO CART</div></div>
<div class="product" style="left:336px"><div class="product-name">brizzles</div><div class="product-card"><div class="product-photo" role="img" aria-label="Wrapped biscuit with an orange quote sticker"><i style="background:var(--orange)"></i></div></div><div class="product-caption">SUCCESS IS OFTEN ACHIEVED BY THOSE WHO DON'T KNOW THAT FAILURE IS INEVITABLE.</div><div class="add-to-cart">ADD TO CART</div></div>
<div class="product" style="left:517px"><div class="product-name">brizzles</div><div class="product-card"><div class="product-photo" role="img" aria-label="Wrapped biscuit with a blue quote sticker"><i style="background:var(--blue)"></i></div></div><div class="product-caption">SUCCESS IS OFTEN ACHIEVED BY THOSE WHO DON'T KNOW THAT FAILURE IS INEVITABLE.</div><div class="add-to-cart">ADD TO CART</div></div>
<div class="product" style="left:699px"><div class="product-name">brizzles</div><div class="product-card"><div class="product-photo" role="img" aria-label="Wrapped biscuit with a red quote sticker"><i style="background:var(--red)"></i></div></div><div class="product-caption">SUCCESS IS OFTEN ACHIEVED BY THOSE WHO DON'T KNOW THAT FAILURE IS INEVITABLE.</div><div class="add-to-cart">ADD TO CART</div></div>

<footer class="site-footer">
  <div class="footer-links"><span>HOME</span><span>|</span><span>ABOUT US</span><span>|</span><span>PRODUCTS</span><span>|</span><span>SEND US A SIGN</span><span>|</span><span>CONTACT US</span></div>
  <div class="copyright">COPYRIGHTS © 2013. BRIZZLE. ALL RIGHTS RESERVED</div>
  <div class="follow">FOLLOW US :</div>
  <span class="social" style="left:727px;background:#2b66b0" aria-label="Social link 1"></span>
  <span class="social" style="left:759px;background:#3fb3e6" aria-label="Social link 2"></span>
  <span class="social" style="left:792px;background:#1f6c9e" aria-label="Social link 3"></span>
  <span class="social" style="left:824px;background:#d3202c" aria-label="Social link 4"></span>
</footer>

</body>
</html>
```